Welding company needs a business card

We are looking for a logo and business card.

Contact Information for Business Card

418 Cobblestone Lane
York, PA 17402
410-555-0173
Rmfabworksco@quorvamail.com

```html
<!DOCTYPE html>
<html lang="en">
<head>
<meta charset="utf-8">
<title>RM Fab Works Co — Business Card</title>
<link rel="stylesheet" href="https://fonts.googleapis.com/css2?family=Montserrat:wght@300;400;500;600&display=swap">
<style>
  :root {
    --page-bg: #e9e6e1;
    --card-dark: #141312;
    --photo-deep: #2a2622;
    --photo-mid: #5c534a;
    --photo-light: #8a7f72;
    --ink: #ffffff;
    --ink-soft: rgba(255,255,255,0.85);
    --rule: rgba(255,255,255,0.75);
  }
  html, body {
    margin: 0;
    width: 1200px;
    height: 1023px;
    overflow: hidden;
    background: var(--page-bg);
  }
  .canvas {
    position: relative;
    width: 1200px;
    height: 1023px;
  }
  .card {
    position: absolute;
    left: 100px;
    top: 226px;
    width: 1000px;
    height: 571px;
    border-radius: 22px;
    overflow: hidden;
    background: var(--card-dark);
    box-shadow: 0 18px 40px rgba(0,0,0,0.25);
    font-family: "Montserrat", sans-serif;
    color: var(--ink);
  }
  .card-photo {
    position: absolute;
    inset: 0;
    background:
      radial-gradient(ellipse 60% 55% at 60% 58%, var(--photo-light) 0%, var(--photo-mid) 45%, transparent 80%),
      linear-gradient(180deg, var(--card-dark) 0%, var(--photo-deep) 35%, var(--photo-deep) 75%, var(--card-dark) 100%);
  }
  .card-shade {
    position: absolute;
    inset: 0;
    background: linear-gradient(180deg, rgba(0,0,0,0.35) 0%, rgba(0,0,0,0.1) 40%, rgba(0,0,0,0.25) 100%);
  }
  .brand {
    position: absolute;
    left: 70px;
    top: 262px;
    width: 480px;
    font-weight: 600;
    font-size: 40px;
    line-height: 1.1;
    letter-spacing: 1px;
    text-transform: uppercase;
    white-space: nowrap;
  }
  .divider {
    position: absolute;
    left: 585px;
    top: 150px;
    width: 1px;
    height: 220px;
    background: var(--rule);
  }
  .contact {
    position: absolute;
    left: 615px;
    top: 150px;
    width: 360px;
  }
  .person-name {
    margin: 0;
    font-weight: 500;
    font-size: 28px;
    letter-spacing: 2px;
    text-transform: uppercase;
  }
  .person-role {
    margin: 4px 0 24px;
    font-weight: 300;
    font-size: 19px;
    color: var(--ink-soft);
  }
  .contact-line {
    margin: 0 0 6px;
    font-weight: 300;
    font-size: 19px;
    color: var(--ink-soft);
    display: flex;
    align-items: center;
    gap: 10px;
    white-space: nowrap;
  }
  .contact-line svg { width: 14px; height: 14px; flex: none; }
  .address { margin-bottom: 16px; }
  .address .contact-line { margin-bottom: 2px; }
</style>
</head>
<body>
<div class="canvas">
  <section class="card">
    <div class="card-photo" role="img" aria-label="Workshop photo of a welded steel seam with a grinder in a dim fabrication shop"></div>
    <div class="card-shade"></div>

    <div class="brand">RM Fab Works Co</div>

    <div class="divider"></div>

    <div class="contact">
      <p class="person-name">Daniel Reyes</p>
      <p class="person-role">Director</p>
      <div class="address">
        <p class="contact-line">418 Cobblestone Lane</p>
        <p class="contact-line">York, PA 17402</p>
      </div>
      <p class="contact-line">
        <svg viewBox="0 0 16 16" aria-hidden="true"><path fill="#fff" d="M3.6 1.5l2.2 2.6-1.3 1.6c.9 2 2.4 3.5 4.4 4.4l1.6-1.3 2.6 2.2-1.2 2.3C6.6 13 3 9.4 1.3 2.7z"/></svg>
        410-555-0173
      </p>
      <p class="contact-line">
        <svg viewBox="0 0 16 16" aria-hidden="true"><rect x="1.5" y="3.5" width="13" height="9" fill="none" stroke="#fff" stroke-width="1.4"/><path d="M1.5 3.5l6.5 5 6.5-5" fill="none" stroke="#fff" stroke-width="1.4"/></svg>
        Rmfabworksco@quorvamail.com
      </p>
    </div>
  </section>
</div>
</body>
</html>
```